Business Card Design Project

We need a business card design for a new construction company called 'KORVA HOLDINGS PTY.LTD' We run a construction based company for high end market homes in melbourne, we want something that looks professional and eye catching.The card needs to have a strong design to it something modern as the company name explains "korva." The final design should communicate professionalism and a strong image to our customers on the quality of our work.
On the business card i need
Name: Marek Holtvay
Mob:0417295031
Email:korva.holdings@mailbrook.example
Domestic/Residential/Commercial

```html
<!DOCTYPE html>
<html lang="en">
<head>
<meta charset="utf-8">
<title>Korva Holdings – Business Cards</title>
<link rel="stylesheet" href="https://fonts.googleapis.com/css2?family=Open+Sans:wght@400;600;700&display=swap">
<style>
  :root {
    --stage: #3a3a3c;
    --ink: #1c1c1d;
    --paper: #ffffff;
    --brand-red: #e0262b;
    --muted-light: #d9d9d9;
    --muted-dark: #3d3d3d;
    --card-w: 520px;
    --card-h: 300px;
  }
  * { box-sizing: border-box; margin: 0; padding: 0; }
  html, body {
    width: 1200px; height: 1065px; overflow: hidden;
    background: var(--stage);
    font-family: "Open Sans", Arial, sans-serif;
  }
  .stage { position: relative; width: 1200px; height: 1065px; }

  .card {
    position: absolute;
    width: var(--card-w); height: var(--card-h);
    overflow: hidden;
    box-shadow: 0 12px 28px rgba(0,0,0,.45);
  }
  .card--dark  { left: 70px;  top: 390px; background: var(--ink); color: var(--paper); }
  .card--light { left: 620px; top: 150px; background: var(--paper); color: var(--ink); }
  .card--back  { left: 620px; top: 660px; background: var(--brand-red); color: var(--paper); }

  .brand { position: absolute; left: 34px; top: 30px; }
  .brand__name {
    font-weight: 700; font-size: 50px; line-height: 1; letter-spacing: -1px;
    text-transform: lowercase;
  }
  .brand__sub {
    font-weight: 600; font-size: 9.5px; letter-spacing: 1.6px; margin-top: 4px;
  }

  .person { position: absolute; left: 34px; top: 148px; }
  .person__name { color: var(--brand-red); font-size: 21px; font-weight: 400; }
  .person__services { font-size: 12px; margin-top: 4px; }

  .contact {
    position: absolute; left: 34px; top: 222px;
    display: grid; grid-template-columns: 14px 3px 1fr; column-gap: 8px; row-gap: 4px;
    font-size: 12px; align-items: center;
  }
  .contact__label { font-weight: 600; }
  .contact__rule { background: var(--brand-red); height: 100%; grid-row: span 2; grid-column: 2; }

  .card--dark .person__services,
  .card--dark .contact { color: var(--muted-light); }
  .card--light .person__services,
  .card--light .contact { color: var(--muted-dark); }
  .card--light .contact { grid-template-columns: 3px 1fr; }
  .card--light .contact__rule { grid-column: 1; }

  .accent { position: absolute; right: 0; top: 0; }

  .card--back .brand {
    left: 0; right: 0; top: 100px; text-align: center;
  }
  .card--back .brand__name { font-size: 72px; }
  .card--back .brand__sub { font-size: 12px; letter-spacing: 3px; margin-top: 6px; }
</style>
</head>
<body>
<main class="stage">

  <section class="card card--dark" aria-label="Business card front, dark">
    <svg class="accent" width="200" height="300" viewBox="0 0 200 300" aria-hidden="true">
      <rect x="110" y="40" width="48" height="260" fill="var(--paper)"/>
      <rect x="62" y="190" width="34" height="34" fill="var(--brand-red)"/>
    </svg>
    <div class="brand">
      <div class="brand__name">korva</div>
      <div class="brand__sub">HOLDINGS PTY.LTD</div>
    </div>
    <div class="person">
      <div class="person__name">Marek Holtvay</div>
      <div class="person__services">Domestic | Residential | Commercial</div>
    </div>
    <div class="contact">
      <span class="contact__label">T</span><span class="contact__rule"></span><span>+04 172 95 031</span>
      <span class="contact__label">E</span><span>korva.holdings@mailbrook.example</span>
    </div>
  </section>

  <section class="card card--light" aria-label="Business card front, light">
    <svg class="accent" width="200" height="300" viewBox="0 0 200 300" aria-hidden="true">
      <rect x="110" y="40" width="48" height="260" fill="var(--ink)"/>
      <rect x="62" y="190" width="34" height="34" fill="var(--brand-red)"/>
    </svg>
    <div class="brand">
      <div class="brand__name">korva</div>
      <div class="brand__sub">HOLDINGS PTY.LTD</div>
    </div>
    <div class="person">
      <div class="person__name">Marek Holtvay</div>
      <div class="person__services">Domestic | Residential | Commercial</div>
    </div>
    <div class="contact">
      <span class="contact__rule"></span><span>+04 172 95 031</span>
      <span>korva.holdings@mailbrook.example</span>
    </div>
  </section>

  <section class="card card--back" aria-label="Business card back">
    <div class="brand">
      <div class="brand__name">korva</div>
      <div class="brand__sub">HOLDINGS PTY.LTD</div>
    </div>
  </section>

</main>
</body>
</html>
```